Mar-wick Sky Harbor Custom Brokers Limited

The Company deals with:
shipping
logistic
imports
Export
customs clearance (customs broker services); and
customers can shop online and we take care of the shipment from the United States of America to Jamaica.
(we offer freight forwarding services from USA to Kingston Jamaica
Our tagline is : Creating Waves in the Logistic Industry.
Address: Shop 9 Birchfield Trade Centre, 227-229 Welland Avenue Kingston 8, Jamaica West Indies Telephone: (876)555-0193
Example of what we required can be seem: www.swiftparcelhubexample.com

```html
<!DOCTYPE html>
<html lang="en">
<head>
<meta charset="utf-8">
<title>Services — Mar-wick Sky Harbor Custom Brokers Limited</title>
<link href="https://fonts.googleapis.com/css2?family=Poppins:wght@400;500;600;700&display=swap" rel="stylesheet">
<style>
:root{
  --navy:#0b2d57;
  --gold:#eaab00;
  --white:#ffffff;
  --field:#efefef;
  --hero-a:#ece9df;
  --hero-b:#c9b08a;
}
*{margin:0;padding:0;box-sizing:border-box}
html,body{width:706px;height:1200px;overflow:hidden;background:var(--white)}
body{position:relative;font-family:'Poppins',sans-serif;color:var(--navy)}
.abs{position:absolute}
.brand{display:flex;align-items:center;gap:4px;font-weight:600;font-size:9px;white-space:nowrap}
.brand-dot{width:12px;height:12px;border-radius:50%;background:var(--gold)}
.site-header .brand{left:92px;top:27px;color:var(--navy)}
.nav a{position:absolute;top:29px;font-size:6.3px;color:var(--navy);text-decoration:none}
.nav a.active{color:var(--gold)}
.btn-signup{left:560px;top:24px;width:53px;height:18px;border-radius:9px;background:var(--gold);font-size:6.5px;font-weight:600;display:flex;align-items:center;justify-content:center}
.hero{left:0;top:66px;width:706px;height:353px;background:linear-gradient(90deg,var(--hero-a) 0%,#e3ddcd 40%,#b9a27f 75%,var(--hero-b) 100%)}
.hero-title{left:93px;top:222px;font-size:33px;font-weight:400;letter-spacing:.5px;white-space:nowrap}
.section-title{left:0;width:706px;top:459px;text-align:center;font-size:18px;font-weight:500;letter-spacing:.4px}
.service{position:absolute;width:140px;margin-left:-70px;text-align:center}
.service .circle{width:88px;height:88px;border-radius:50%;background:var(--navy);margin:0 auto;display:flex;align-items:center;justify-content:center}
.service h3{font-size:9.5px;font-weight:600;margin-top:16px;letter-spacing:.2px}
.service p{font-size:7.4px;line-height:8.6px;margin-top:5px}
.btn-pickup{left:287px;top:890px;width:132px;height:22px;border-radius:11px;background:var(--gold);font-size:6px;font-weight:700;display:flex;align-items:center;justify-content:center;letter-spacing:.2px}
.site-footer{left:0;top:956px;width:706px;height:244px;background:var(--navy);color:var(--white)}
.site-footer .brand{left:92px;top:58px;color:var(--white)}
.rule{height:1px;width:124px;left:92px;background:rgba(255,255,255,.25)}
.f-head{font-size:7.3px;font-weight:600}
.f-text{font-size:6.3px;line-height:9px}
.links a{position:absolute;left:307px;font-size:6.3px;color:var(--white);text-decoration:none}
.newsletter-field{left:437px;top:73px;width:176px;height:22px;border-radius:11px;background:var(--field);color:#555;font-size:6.3px;padding-left:9px;display:flex;align-items:center}
.btn-submit{left:569px;top:73px;width:44px;height:22px;border-radius:11px;background:var(--gold);color:var(--navy);font-size:6.3px;font-weight:700;display:flex;align-items:center;justify-content:center}
</style>
</head>
<body>

<header class="site-header">
  <div class="abs brand"><span class="brand-dot"></span>Mar-wick Sky Harbor</div>
  <nav class="nav">
    <a style="left:277px">Home</a>
    <a class="active" style="left:323px">Services</a>
    <a style="left:378px">About</a>
    <a style="left:424px">Contact</a>
    <a style="left:478px">FAQs</a>
    <a style="left:521px">Login</a>
  </nav>
  <div class="abs btn-signup">Sign Up</div>
</header>

<section class="abs hero" role="img" aria-label="Photo of a woman with a clipboard checking parcels in a warehouse"></section>
<div class="abs hero-title">Home &#8250; Services</div>

<h2 class="abs section-title">What We Do</h2>

<div class="service" style="left:154px;top:508px">
  <div class="circle"><svg width="34" height="30" viewBox="0 0 34 30" fill="#fff"><rect x="0" y="0" width="9" height="8"/><rect x="0" y="10" width="9" height="8"/><rect x="0" y="20" width="9" height="8"/><rect x="11" y="4" width="12" height="20"/><path d="M23 12h6l4 6v8H23z"/><circle cx="26" cy="27" r="3" fill="#0b2d57" stroke="#fff" stroke-width="1.5"/></svg></div>
  <h3>Shipping</h3>
  <p>Lorem ipsum dolor sit amet,<br>consectetur adipiscing elit, sed<br>do eiusmod tempor incididunt ut</p>
</div>
<div class="service" style="left:354px;top:508px">
  <div class="circle"><svg width="32" height="32" viewBox="0 0 32 32" fill="#fff"><rect x="10" y="2" width="16" height="20" rx="1"/><rect x="13" y="6" width="10" height="1.5" fill="#0b2d57"/><rect x="13" y="10" width="10" height="1.5" fill="#0b2d57"/><rect x="13" y="14" width="10" height="1.5" fill="#0b2d57"/><rect x="0" y="16" width="9" height="7"/><rect x="0" y="24" width="9" height="8"/><rect x="10" y="24" width="9" height="8"/><path d="M18 22l12-6 1 2-12 6z"/></svg></div>
  <h3>Logistics</h3>
  <p>Lorem ipsum dolor sit amet,<br>consectetur adipiscing elit, sed<br>do eiusmod tempor incididunt ut</p>
</div>
<div class="service" style="left:552px;top:508px">
  <div class="circle"><svg width="34" height="32" viewBox="0 0 34 32" fill="#fff"><rect x="3" y="0" width="2" height="22"/><path d="M0 20h8l-4 6z"/><path d="M13 0h2v5h3l-4 4-4-4h3z"/><path d="M25 0h2v5h3l-4 4-4-4h3z"/><rect x="11" y="11" width="9" height="8"/><rect x="22" y="11" width="9" height="8"/><rect x="11" y="20" width="9" height="8"/><rect x="22" y="20" width="9" height="8"/><rect x="0" y="29" width="34" height="1.5"/></svg></div>
  <h3>Import</h3>
  <p>Lorem ipsum dolor sit amet,<br>consectetur adipiscing elit, sed<br>do eiusmod tempor incididunt ut</p>
</div>

<div class="service" style="left:156px;top:694px">
  <div class="circle"><svg width="34" height="32" viewBox="0 0 34 32" fill="#fff"><path d="M4 0l4 4H5v6H3V4H0z"/><path d="M16 0l4 4h-3v6h-2V4h-3z"/><rect x="0" y="11" width="9" height="8"/><rect x="11" y="11" width="9" height="8"/><rect x="0" y="20" width="9" height="8"/><rect x="11" y="20" width="9" height="8"/><path d="M28 0l4 5h-3v23h-2V5h-3z"/><rect x="0" y="29" width="34" height="1.5"/></svg></div>
  <h3>Export</h3>
  <p>Lorem ipsum dolor sit amet,<br>consectetur adipiscing elit, sed<br>do eiusmod tempor incididunt ut</p>
</div>
<div class="service" style="left:356px;top:694px">
  <div class="circle"><svg width="34" height="32" viewBox="0 0 34 32" fill="#fff"><rect x="0" y="0" width="18" height="30" rx="1"/><rect x="3" y="4" width="3" height="3" fill="#0b2d57"/><rect x="8" y="5" width="8" height="1.5" fill="#0b2d57"/><rect x="3" y="11" width="3" height="3" fill="#0b2d57"/><rect x="8" y="12" width="8" height="1.5" fill="#0b2d57"/><rect x="3" y="18" width="3" height="3" fill="#0b2d57"/><rect x="8" y="19" width="8" height="1.5" fill="#0b2d57"/><path d="M25 0h2v7h3l-4 5-4-5h3z"/><path d="M16 16h18v16H16z"/><rect x="24" y="16" width="1.5" height="16" fill="#0b2d57"/></svg></div>
  <h3>Custom Clearance</h3>
  <p>Lorem ipsum dolor sit amet,<br>consectetur adipiscing elit, sed<br>do eiusmod tempor incididunt ut</p>
</div>
<div class="service" style="left:551px;top:694px">
  <div class="circle"><svg width="34" height="34" viewBox="0 0 34 34" fill="#fff"><rect x="13" y="0" width="8" height="2"/><rect x="11" y="4" width="12" height="4"/><rect x="8" y="10" width="18" height="5"/><rect x="6" y="17" width="22" height="6"/><path d="M0 25h34l-5 7H5z"/><rect x="0" y="33" width="34" height="1"/></svg></div>
  <h3>Frieght Forwarding</h3>
  <p>Lorem ipsum dolor sit amet,<br>consectetur adipiscing elit, sed<br>do eiusmod tempor incididunt ut</p>
</div>

<div class="abs btn-pickup">SCHEDULE A PICK-UP</div>

<footer class="abs site-footer">
  <div class="abs brand"><span class="brand-dot"></span>Mar-wick Sky Harbor</div>
  <div class="abs rule" style="top:102px"></div>
  <div class="abs f-head" style="left:92px;top:113px">Address</div>
  <div class="abs f-text" style="left:92px;top:127px">Shop 9 Birchfield Trade Centre,<br>227-229 Welland Avenue Kingston 8,<br>Jamaica West Indies</div>
  <div class="abs rule" style="top:167px"></div>
  <div class="abs f-head" style="left:92px;top:178px">Telephone</div>
  <div class="abs f-text" style="left:92px;top:192px">(876)555-0193</div>

  <div class="abs f-head" style="left:307px;top:42px">Quick Links</div>
  <nav class="links">
    <a style="top:57px">About</a>
    <a style="top:75px">Services</a>
    <a style="top:92px">FAQs</a>
    <a style="top:110px">Contact</a>
    <a style="top:128px">Jobs</a>
  </nav>

  <div class="abs f-head" style="left:437px;top:42px">Join Our Newsletter</div>
  <div class="abs f-text" style="left:436px;top:57px">Lorem ipsum dolor sit amet, consectetur</div>
  <div class="abs newsletter-field">Your Email</div>
  <div class="abs btn-submit">SUBMIT</div>
</footer>

</body>
</html>
```